Renaldo's Motorworks landing page to Dealership page, Rental Car Page, and Auto Body page.

I'm looking for my website to have RenaldosMotor.com be the landing page. From there visitors will have the option to visit three pages. My auto dealer page, of which I will provide an example of how I'd like it done. Auto body page, where I will fill in the text. The rental car page. Basically on the auto dealer and rental page I'll need the ability to add vehicles and delete as I need. Otherwise, its a pretty straightforward site. Nothing extensive. I already have the logo design from a previous project on here completed and can provide. If more funded needed for page capabilities, I can provide. I do have an account with HostPeak, with renaldosmotor.com already under them.

Target Market(s)

Automotive

Industry/Entity Type

Auto body repair, dealership, rental car.

Coding

Coded - Design and coding required

Number of Pages Required

4 page

Font styles to use
Sans Serif

Colors
0054AA
0677BA
7BADD7
CADEEF
E8F1F8

Requirements
Must have
• My logo Renaldos Motorworks at the top. Be creative with pics in the background of cars.
Nice to have
• Ease of use with being able to add vehicles for sale, and rental cars.
Should not have
• Nothing complex, would like to get in and out. Nothing to extensive on the designs of the pages, simple but attractive.

```html
<!DOCTYPE html>
<html lang="en">
<head>
<meta charset="utf-8">
<title>Renaldo's Motorworks</title>
<link href="https://fonts.googleapis.com/css2?family=Heebo:wght@300;400;500;600;700&family=Roboto+Condensed:wght@400;500&display=swap" rel="stylesheet">
<style>
:root{
  --blue:#0054AA;
  --blue-2:#0677BA;
  --blue-3:#7BADD7;
  --blue-4:#CADEEF;
  --blue-5:#E8F1F8;
  --ink:#1d1d1f;
  --text:#444;
  --dark:#2a292b;
  --white:#fff;
}
*{margin:0;padding:0;box-sizing:border-box}
html,body{width:1200px;height:2993px;overflow:hidden}
body{position:relative;font-family:'Heebo',sans-serif;color:var(--ink);background:var(--white)}
.abs{position:absolute}
.center{left:0;width:1200px;text-align:center}
.btn{position:absolute;display:flex;align-items:center;justify-content:center;border-radius:16px;font-size:10px;font-weight:500}
.btn-blue{background:var(--blue);color:#fff}
.btn-white{background:#fff;color:var(--blue)}
.eyebrow{font-size:11px;color:var(--blue);font-weight:500}
.heading{font-size:23px;font-weight:500;color:var(--ink)}
/* header */
.header{top:0;left:0;width:1200px;height:95px;background:#fff}
.brand{left:78px;top:34px;display:flex;align-items:center;gap:8px}
.brand-dot{width:14px;height:14px;border-radius:50%;background:var(--blue)}
.brand-name{font-size:20px;font-weight:700;color:var(--blue)}
.nav{left:330px;top:42px;display:flex;gap:27px;font-size:10px;color:#333}
.nav .active{color:var(--blue)}
.head-phone{left:870px;top:30px;font-family:'Roboto Condensed',sans-serif;font-size:16px;color:#222;display:flex;align-items:center;gap:5px}
.head-mail{left:858px;top:52px;font-size:9px;color:#333}
.head-mail b{color:var(--blue);font-weight:400}
.social{width:24px;height:24px;border-radius:50%}
/* hero */
.hero{top:95px;left:0;width:1200px;height:432px;background:linear-gradient(180deg,#1d2a3c 0%,#4a6787 40%,#8a8f7a 62%,#3d4a2e 78%,#3a3a3c 100%)}
.hero-title{font-size:38px;font-weight:400;color:#fff;line-height:44px}
.hero-word{font-size:190px;font-weight:700;color:rgba(255,255,255,.28);letter-spacing:6px;line-height:190px}
.hero-cars{left:215px;top:220px;width:760px;height:212px;border-radius:60px 60px 0 0;background:linear-gradient(90deg,#a5121c 0%,#d3283a 35%,#1e3f9a 60%,#123071 100%);opacity:.85}
.search-tab{top:504px;left:204px;width:296px;height:24px;background:var(--blue-2);color:#fff;font-size:15px;padding:4px 0 0 22px}
.search-tab b{font-style:italic}
.search-bar{top:527px;left:0;width:1200px;height:48px;background:var(--blue-2)}
.select{top:538px;height:28px;width:192px;border-radius:14px;background:#fff;font-size:9px;color:#555;padding:9px 0 0 17px}
.select svg{position:absolute;right:14px;top:11px}
.search-btn{top:538px;left:913px;width:191px;height:28px;border-radius:14px;background:#1f1e20;color:#fff;font-size:9px;font-weight:500;display:flex;align-items:center;justify-content:center}
/* welcome */
.welcome-bg{top:960px;left:0;width:1200px;height:190px;background:linear-gradient(180deg,#fff 0%,#dfe7ef 45%,#8ea3b8 75%,#c4d0dc 100%)}
.intro{top:692px;left:305px;width:590px;text-align:center;font-size:10px;line-height:14.5px;color:#444}
.rule{top:795px;left:204px;width:792px;height:1px;background:#ddd}
.feature{top:875px;width:180px;height:167px;background:#fff;box-shadow:0 2px 10px rgba(0,0,0,.06);text-align:center}
.feature-icon{position:absolute;left:54px;top:-30px;width:72px;height:72px;border-radius:50%;background:#f1f2f4;display:flex;align-items:center;justify-content:center}
.feature h3{margin-top:55px;font-size:11px;font-weight:600}
.feature p{margin:18px auto 0;width:150px;font-size:9px;line-height:14.5px;color:#555}
.ask{top:1074px;font-size:15px;font-weight:500}
.ask-phone{top:1094px;font-family:'Roboto Condensed',sans-serif;font-size:24px;color:var(--blue)}
/* services */
.services{top:1150px;left:0;width:1200px;height:271px}
.svc{width:390px;text-align:center;color:#fff}
.svc h3{font-size:21px;font-weight:600}
.svc p{margin:4px auto 0;width:330px;font-size:9.5px;line-height:14.5px}
.svc .btn{position:relative;margin:13px auto 0;width:120px;height:30px;border-radius:15px}
/* offers */
.car{top:1545px;width:180px;height:281px;background:#fff;box-shadow:0 2px 10px rgba(0,0,0,.08)}
.car-photo{height:149px}
.car-photo.white{background:linear-gradient(160deg,#8a6a4e 0%,#d9d9d9 45%,#f5f5f5 70%,#9a9a9a 100%)}
.car-photo.truck{background:linear-gradient(160deg,#667385 0%,#c9cdd3 45%,#e6e7e9 70%,#7f8288 100%)}
.car-actions{position:absolute;right:10px;top:8px;display:flex;flex-direction:column;gap:6px}
.car-actions span{width:22px;height:22px;border-radius:50%;background:#fff;display:flex;align-items:center;justify-content:center}
.car-actions span.on{background:var(--blue-2)}
.price{position:absolute;left:18px;top:139px;height:24px;width:90px;background:var(--blue);clip-path:polygon(0 0,75% 0,100% 100%,0 100%);color:#fff;font-family:'Roboto Condensed',sans-serif;font-size:15px;padding:2px 0 0 7px}
.car h4{position:absolute;left:18px;top:171px;font-size:10.5px;font-weight:500;line-height:16px;color:#222}
.car hr{position:absolute;left:18px;top:210px;width:144px;border:0;border-top:1px solid #ddd}
.specs{position:absolute;left:18px;top:220px;font-size:9px;line-height:14.5px;color:#555;list-style:none}
.specs li::before{content:"";display:inline-block;width:7px;height:7px;border:1px solid var(--blue-2);border-radius:2px;margin-right:6px}
.round-arrow{width:24px;height:24px}
/* band */
.band{top:1947px;left:0;width:1200px;height:150px;background:linear-gradient(90deg,#1f2023 0%,#2e3035 55%,#4a4c52 80%,#2b2c30 100%)}
.band-text{left:204px;top:2006px;font-size:23px;color:#fff;font-weight:400}
/* reviews */
.quote{top:2219px;left:345px;width:510px;text-align:center;font-size:14.5px;font-style:italic;font-weight:300;line-height:26.5px;color:#444}
.quote sup{color:var(--blue-2);font-size:12px;font-style:normal}
.reviewer{top:2339px;font-size:11px;font-weight:500}
.avatar{border-radius:50%;background:radial-gradient(circle,#e9e1d7 0%,#c9c2bb 100%)}
/* footer */
.footer{top:2546px;left:0;width:1200px;height:447px;background:var(--dark)}
.field{left:204px;width:365px;height:28px;border-radius:14px;background:#6b6a6c;color:#fff;font-size:9px;padding:9px 0 0 13px}
.contact{left:630px;color:#fff;font-size:9.5px;line-height:14px}
.contact .label{color:var(--blue-3);font-size:9px}
.contact .phone{font-family:'Roboto Condensed',sans-serif;font-size:15px;color:var(--blue-3)}
.copy{top:2932px;font-size:9px;color:#fff}
</style>
</head>
<body>

<header class="abs header">
  <div class="abs brand"><span class="brand-dot"></span><span class="brand-name">Renaldo's Motorworks</span></div>
  <nav class="abs nav">
    <span class="active">Home</span><span>About</span><span>My Auto Dealer</span><span>Auto Body</span><span>Rental Car</span><span>Reviews</span><span>Contact</span>
  </nav>
  <div class="abs head-phone">
    <svg width="14" height="14" viewBox="0 0 24 24"><path d="M6 3l3 0 2 5-2 2c1 2 3 4 5 5l2-2 5 2v3c0 1-1 2-2 2C10 20 4 14 4 5c0-1 1-2 2-2z" fill="none" stroke="#0054AA" stroke-width="2"/></svg>
    (555)-014-2286
  </div>
  <div class="abs head-mail"><b>e.</b> sales@renaldosmotor.com</div>
  <div class="abs social" style="left:1068px;top:36px;background:#1f1e20" role="img" aria-label="Social profile"></div>
  <div class="abs social" style="left:1097px;top:36px;background:var(--blue-2)" role="img" aria-label="Social profile"></div>
</header>

<section class="abs hero" role="img" aria-label="Red sedan and blue coupe on a road through mountains">
  <div class="abs hero-cars"></div>
</section>
<div class="abs center hero-word" style="top:218px">BUY A CAR!</div>
<h1 class="abs center hero-title" style="top:131px">45,000+ Cars Type &amp; Brands<br>Get Your Best Cars</h1>
<div class="abs search-tab">Find the <b>Right Car</b> for you</div>
<div class="abs search-bar"></div>
<div class="abs select" style="left:96px">Brand<svg width="8" height="5"><path d="M0 0l4 4 4-4" fill="none" stroke="#777"/></svg></div>
<div class="abs select" style="left:300px">Model<svg width="8" height="5"><path d="M0 0l4 4 4-4" fill="none" stroke="#777"/></svg></div>
<div class="abs select" style="left:504px">Year<svg width="8" height="5"><path d="M0 0l4 4 4-4" fill="none" stroke="#777"/></svg></div>
<div class="abs select" style="left:709px">Trim<svg width="8" height="5"><path d="M0 0l4 4 4-4" fill="none" stroke="#777"/></svg></div>
<div class="abs search-btn">Find the Right Car for you</div>

<div class="abs welcome-bg" role="img" aria-label="Misty snow-capped mountain range"></div>
<div class="abs center eyebrow" style="top:633px">Welcome to</div>
<h2 class="abs center heading" style="top:649px">Renaldo's Motorworks</h2>
<p class="abs intro">Lorem Ipsum is simply dummy text of the printing and typesetting industry. Lorem Ipsum has been the industry's standard dummy text ever since the 1500s, when an unknown printer took a galley of type and scrambled it to make a type specimen book. It has survived not only five centuries, but also the leap into electronic typesetting essentially unchanged. It was popularised in the 1960s with the release ...</p>
<div class="abs rule"></div>
<div class="btn btn-blue" style="left:546px;top:781px;width:107px;height:28px">About Us</div>

<div class="abs feature" style="left:204px">
  <div class="feature-icon"><svg width="30" height="30" viewBox="0 0 30 30" fill="none" stroke="#0054AA" stroke-width="1.6"><path d="M15 3v12M18 6h-4a2 2 0 000 4h2a2 2 0 010 4h-4"/><path d="M3 20c3-2 6-2 9 0h6c1 0 1 2 0 2h-5M3 24c4 2 9 3 14 1l9-5"/></svg></div>
  <h3>Easy Financing</h3><p>It is a long established fact that a reader will be distracted by the readable content of a page when looking layout.</p>
</div>
<div class="abs feature" style="left:408px">
  <div class="feature-icon"><svg width="30" height="30" viewBox="0 0 30 30" fill="none" stroke="#0054AA" stroke-width="1.6"><rect x="5" y="7" width="20" height="16" rx="3"/><path d="M5 15h20M9 19h2M19 19h2M8 23v3M22 23v3"/></svg></div>
  <h3>Huge Selection</h3><p>It is a long established fact that a reader will be distracted by the readable content of a page when looking layout.</p>
</div>
<div class="abs feature" style="left:612px">
  <div class="feature-icon"><svg width="30" height="30" viewBox="0 0 30 30" fill="none" stroke="#0054AA" stroke-width="1.6"><circle cx="15" cy="10" r="6"/><path d="M5 27c0-6 4-10 10-10s10 4 10 10"/></svg></div>
  <h3>Amazing Service</h3><p>It is a long established fact that a reader will be distracted by the readable content of a page when looking layout.</p>
</div>
<div class="abs feature" style="left:817px">
  <div class="feature-icon"><svg width="30" height="30" viewBox="0 0 30 30" fill="none" stroke="#0054AA" stroke-width="1.6"><rect x="4" y="13" width="5" height="13"/><path d="M9 14l5-9c2 0 3 2 2 5l-1 3h8c2 0 3 2 2 4l-3 7c-1 2-2 2-4 2H9"/></svg></div>
  <h3>Our Difference</h3><p>It is a long established fact that a reader will be distracted by the readable content of a page when looking layout.</p>
</div>
<div class="abs center ask">Have any Question? Call Us Today!</div>
<div class="abs center ask-phone">
  <svg width="22" height="20" viewBox="0 0 24 24" style="vertical-align:-2px"><path d="M6 3l3 0 2 5-2 2c1 2 3 4 5 5l2-2 5 2v3c0 1-1 2-2 2C10 20 4 14 4 5c0-1 1-2 2-2z" fill="none" stroke="#0054AA" stroke-width="1.8"/></svg>. (555)-014-2286
</div>

<svg class="abs services" width="1200" height="271" viewBox="0 0 1200 271" role="img" aria-label="Dealer handing over keys, couple at an auto body shop, and a smiling rental car driver">
  <polygon points="0,0 418,0 331,271 0,271" fill="#0a63c2"/>
  <polygon points="428,0 854,0 770,271 341,271" fill="#2b2d33"/>
  <polygon points="864,0 1200,0 1200,271 781,271" fill="#0a66c6"/>
</svg>
<div class="abs svc" style="left:0;top:1230px"><h3>My Auto Dealer</h3><p>It is a long established fact that a reader will be distracted by the readable content of a page when looking at its layout.</p><div class="btn btn-white">Explore More</div></div>
<div class="abs svc" style="left:405px;top:1230px"><h3>Auto Body</h3><p>It is a long established fact that a reader will be distracted by the readable content of a page when looking at its layout.</p><div class="btn btn-white">Explore More</div></div>
<div class="abs svc" style="left:810px;top:1230px"><h3>Rental Car</h3><p>It is a long established fact that a reader will be distracted by the readable content of a page when looking at its layout.</p><div class="btn btn-white">Explore More</div></div>

<div class="abs center eyebrow" style="top:1479px">Featured Used Car</div>
<h2 class="abs center heading" style="top:1495px">Get Our Best Offers</h2>

<svg class="abs round-arrow" style="left:156px;top:1675px" viewBox="0 0 24 24" fill="none" stroke="#222" stroke-width="1.5"><circle cx="12" cy="12" r="11"/><path d="M17 12H7M11 8l-4 4 4 4"/></svg>
<svg class="abs round-arrow" style="left:1019px;top:1675px" viewBox="0 0 24 24" fill="none" stroke="#0054AA" stroke-width="1.5"><circle cx="12" cy="12" r="11"/><path d="M7 12h10M13 8l4 4-4 4"/></svg>

<article class="abs car" style="left:204px">
  <div class="car-photo white" role="img" aria-label="White sports coupe in a showroom"></div>
  <div class="car-actions"><span class="on"></span><span></span><span></span></div>
  <div class="price">$8 990</div>
  <h4>2010 Stellan Motors<br>SLX 500</h4><hr>
  <ul class="specs"><li>Mileage: 147238mi</li><li>Transmission: Manual</li><li>Fuel: Pretrol</li></ul>
</article>
<article class="abs car" style="left:408px">
  <div class="car-photo truck" role="img" aria-label="Silver pickup truck on a dealer lot"></div>
  <div class="car-actions"><span></span><span></span><span></span></div>
  <div class="price">$8 990</div>
  <h4>2010 Stellan Motors<br>SLX 500</h4><hr>
  <ul class="specs"><li>Mileage: 147238mi</li><li>Transmission: Manual</li><li>Fuel: Pretrol</li></ul>
</article>
<article class="abs car" style="left:612px">
  <div class="car-photo white" role="img" aria-label="White sports coupe in a showroom"></div>
  <div class="car-actions"><span></span><span></span><span></span></div>
  <div class="price">$8 990</div>
  <h4>2010 Stellan Motors<br>SLX 500</h4><hr>
  <ul class="specs"><li>Mileage: 147238mi</li><li>Transmission: Manual</li><li>Fuel: Pretrol</li></ul>
</article>
<article class="abs car" style="left:817px">
  <div class="car-photo truck" role="img" aria-label="Silver pickup truck on a dealer lot"></div>
  <div class="car-actions"><span></span><span></span><span></span></div>
  <div class="price">$8 990</div>
  <h4>2010 Stellan Motors<br>SLX 500</h4><hr>
  <ul class="specs"><li>Mileage: 147238mi</li><li>Transmission: Manual</li><li>Fuel: Pretrol</li></ul>
</article>
<div class="btn btn-blue" style="left:546px;top:1859px;width:107px;height:28px">View All</div>

<div class="abs band" role="img" aria-label="Salesman in a suit handing over car keys"></div>
<div class="abs band-text">Contrary to popular belief, lorem Ipsum simply text.</div>
<div class="btn btn-white" style="left:876px;top:2007px;width:120px;height:30px;border-radius:15px">Contact Us</div>

<div class="abs center eyebrow" style="top:2155px">Latest Reviews</div>
<h2 class="abs center heading" style="top:2171px">Happy Clients Say</h2>
<svg class="abs" style="left:247px;top:2249px" width="14" height="20" viewBox="0 0 14 20"><path d="M11 2L3 10l8 8" fill="none" stroke="#0054AA" stroke-width="1.5"/></svg>
<svg class="abs" style="left:938px;top:2249px" width="14" height="20" viewBox="0 0 14 20"><path d="M3 2l8 8-8 8" fill="none" stroke="#0054AA" stroke-width="1.5"/></svg>
<p class="abs quote"><sup>66</sup> It is a long established fact that a reader will be distracted by the readable content of a page when looking at its layout. the point of using lorem various versions have evolved over the years, sometimes by accident Ipsum is that it has a more-or-less normal... <sup>99</sup></p>
<div class="abs center reviewer">- Standard Chunk -</div>
<div class="abs avatar" style="left:516px;top:2377px;width:42px;height:42px" role="img" aria-label="Client portrait"></div>
<div class="abs avatar" style="left:570px;top:2369px;width:60px;height:60px;border:2px solid var(--blue)" role="img" aria-label="Client portrait"></div>
<div class="abs avatar" style="left:642px;top:2377px;width:42px;height:42px" role="img" aria-label="Client portrait"></div>
<div class="btn btn-blue" style="left:546px;top:2458px;width:108px;height:28px">View All Reviews</div>

<footer class="abs footer"></footer>
<div class="abs center" style="top:2604px;font-size:10px;color:#fff;font-weight:500">Get in Touch</div>
<h2 class="abs center heading" style="top:2620px;color:#fff">Contact Us Today!</h2>
<div class="abs field" style="top:2672px">Your Name</div>
<div class="abs field" style="top:2714px">Email</div>
<div class="abs field" style="top:2756px">Phone</div>
<div class="abs field" style="top:2798px;height:70px">Message ...</div>
<svg class="abs" style="left:525px;top:2868px" width="28" height="28" viewBox="0 0 28 28"><circle cx="14" cy="14" r="14" fill="#0054AA"/><path d="M12 9l5 5-5 5" fill="none" stroke="#fff" stroke-width="1.5"/></svg>

<div class="abs contact" style="top:2670px"><span class="phone">(555)-014-2286</span><br>e. sales@renaldosmotor.com</div>
<div class="abs contact" style="top:2720px"><span class="label">Renaldo's Motorworks</span><br>669 Lorem Ipsum wor Harlow Bay,<br>MI 12345</div>
<div class="abs contact" style="top:2778px"><span class="label">Open Hours</span><br>MON - FRI 8AM - 6PM<br>SAT 8AM - 2PM</div>
<div class="abs social" style="left:632px;top:2846px;width:26px;height:26px;background:var(--blue)" role="img" aria-label="Social profile"></div>
<div class="abs social" style="left:667px;top:2846px;width:26px;height:26px;background:var(--blue-4)" role="img" aria-label="Social profile"></div>
<svg class="abs" style="left:952px;top:2670px" width="44" height="44" viewBox="0 0 44 44" fill="none" stroke="#0054AA" stroke-width="1.6"><path d="M1 8V1h42v7M22 44V10M12 20l10-10 10 10"/></svg>
<div class="abs center copy">© 2021 <b style="font-weight:500">Renaldo's Motorworks</b> &nbsp;|&nbsp; Privacy Policy</div>

</body>
</html>
```